Loomberry AI - Help users create their own recipe for a delicious AI treat!

Our company is an AI startup called Loomberrys. A Loomberry is an easy way to play with data (user can ask questions and get visualized answers about the dataset, sort of like QuillMate). Our users can "bake" their own Loomberrys by combining different sources of data.

We need a page that offers two things (both are required):

(1) TRY A LOOMBERRY --> Present a gallery of pre-made Loomberrys, each of which a user can click on and start playing with inside a popup iFrame. (visually, a Loomberry should be represented by some variation of our logo, attached). Designer does not need to worry about the iFrame popup.

(2) BAKE YOUR OWN LOOMBERRY --> Guide the user through making their own Loomberry recipe. The steps in making a Loomberry are:

A. Pick first ingredient - a Connector that imports the user's own data (visually, we present these options as logos for the Connector source, like Zentor, Pallomix, Brivane KLX, etc.).

B. Pick additional ingredients - the user can choose from 3rd-party cakes to combine with their own data added in (A). (visually, these 3rd-party cake options are presented as "mini" cakes, similar to our logo)

C. Once the ingredients are selected, the user can hit a BAKE button, and an iFrame popup opens, where user can play with the result. Designer does not need to worry about the iFrame popup.

We already have a web page and color scheme that we'd like this page to match (https://www.loomberrys.ai). The designer has freedom to play with format and try variations on the color scheme. The overall design should feel futuristic, fun, but also professional (like our logo).

Target Market(s)

Business users who want an easier way to get answers from large messy data

Industry/Entity Type

Tech/AI

Number of Pages Required

1 page

Font styles to use
Other font styles liked:
• Rubik

Requirements
Must have
• Full page design that matches current website (www.loomberrys.ai) and meets all requirements in the Project Description
Nice to have
• Included in the Project Description
Should not have
• Do not submit any designs that are too cartoonish or would not appeal to a business user

```html
<!DOCTYPE html>
<html lang="en">
<head>
<meta charset="utf-8">
<title>Loomberry AI</title>
<link href="https://fonts.googleapis.com/css2?family=Rubik:wght@300;400;500;700&display=swap" rel="stylesheet">
<style>
:root{
  --bg:#0e1628;
  --ink:#ffffff;
  --muted:#c9cfdb;
  --dim:#6d7588;
  --cyan:#16e6f2;
  --lime:#f4f23c;
  --pink:#e06aa8;
  --dark:#0b1020;
  --line:#d6dc45;
}
*{margin:0;padding:0;box-sizing:border-box}
html,body{width:813px;height:1200px;overflow:hidden;background:#fff}
body{font-family:'Rubik',sans-serif;color:var(--ink);position:relative}
.page{
  position:absolute;left:212.7px;top:0;width:750px;height:2324px;
  transform:scale(0.51619);transform-origin:0 0;overflow:hidden;
  background:
    radial-gradient(circle at 40px 200px,rgba(130,150,40,.75),transparent 120px),
    radial-gradient(circle at 700px 200px,rgba(15,120,140,.8),transparent 150px),
    radial-gradient(circle at 20px 700px,rgba(110,70,130,.7),transparent 150px),
    radial-gradient(circle at 300px 600px,rgba(140,60,140,.35),transparent 120px),
    radial-gradient(circle at 160px 1000px,rgba(20,100,130,.55),transparent 110px),
    radial-gradient(circle at 740px 1120px,rgba(150,160,40,.7),transparent 160px),
    radial-gradient(circle at 20px 1400px,rgba(110,70,60,.7),transparent 130px),
    radial-gradient(circle at 170px 1640px,rgba(140,160,40,.6),transparent 110px),
    radial-gradient(circle at 690px 1630px,rgba(120,70,130,.7),transparent 150px),
    radial-gradient(circle at 740px 2050px,rgba(15,120,140,.7),transparent 130px),
    radial-gradient(circle at 30px 2120px,rgba(110,70,130,.5),transparent 120px),
    var(--bg);
}
.abs{position:absolute}
.center{left:0;right:0;text-align:center}
.brand{display:flex;align-items:center;gap:6px;font-weight:300;color:var(--ink)}
.brand-mark{width:14px;height:14px;background:var(--cyan);border-radius:2px}
.site-brand{left:31px;top:24px;font-size:17px}
.nav{right:31px;top:30px;display:flex;gap:17px;font-size:8px;font-weight:500}
.nav a{color:var(--ink);text-decoration:none}
.nav .active{color:var(--cyan);border-bottom:1px solid var(--pink);padding-bottom:4px}
.headline{top:138px;font-size:33px;font-weight:700;line-height:39px}
.subhead{top:247px;font-size:20px;font-weight:400;line-height:25px}
.lede{top:336px;left:120px;right:120px;font-size:12px;font-weight:300;line-height:15px}
.lede b{color:var(--lime);font-weight:700}
.rule{height:1px;width:106px;left:322px;background:linear-gradient(90deg,var(--cyan),var(--lime))}
.intro{top:445px;font-size:20px;line-height:25px}
.grad-text{background:linear-gradient(90deg,var(--cyan),var(--lime),var(--pink));-webkit-background-clip:text;background-clip:text;color:transparent}
.glow-frame{padding:3px;border-radius:9px;background:linear-gradient(90deg,var(--cyan),var(--lime))}
.glow-frame>div{width:100%;height:100%;border-radius:7px}
.video{left:29px;top:571px;width:316px;height:184px}
.video-fill{background:#000;display:flex;align-items:center;justify-content:center}
.btn{display:flex;align-items:center;justify-content:center;border-radius:6px;font-size:14px}
.btn-solid{background:linear-gradient(90deg,var(--cyan),var(--lime));color:var(--dark)}
.btn-ghost{border:1px solid var(--cyan);color:var(--ink)}
.demo{left:106px;top:770px;width:163px;height:37px}
.wait{left:106px;top:823px;width:163px;height:38px}
.pill{background:#fff;color:var(--dark);font-weight:700;font-size:12px;border-radius:10px;display:flex;align-items:center;justify-content:center}
.try-pill{left:481px;top:536px;width:163px;height:19px}
.screen{left:404px;top:571px;width:317px;height:184px}
.screen-fill{background:linear-gradient(160deg,#d7e6fb,#a8c6f1 55%,#cfe0f8)}
.arrow{top:771px;width:12px;height:16px}
.dots{left:538px;top:776px;display:flex;gap:5px}
.dots i{width:5px;height:5px;border-radius:50%;background:#3d6f8a}
.dots i.on{background:var(--cyan)}
.sample{top:810px;width:90px;text-align:center;font-size:7px}
.sample .shape{width:52px;height:28px;margin:0 auto 6px;background:#5a6172;border-radius:4px}
.sample .shape.round{width:28px;border-radius:50%}
.sample.on{color:var(--cyan)}
.sample.on span{border-bottom:1px solid var(--pink);padding-bottom:3px}
.sample.off{color:var(--dim)}
.bake-pill{left:267px;top:987px;width:214px;height:19px}
.card{left:145px;width:458px;height:210px;padding:2px;border-radius:9px;background:linear-gradient(90deg,var(--cyan),var(--pink))}
.card-in{width:100%;height:100%;border-radius:7px;background:var(--bg);text-align:center;padding:20px 40px 0}
.card h2{font-size:20px;font-weight:400;margin-bottom:20px;letter-spacing:.3px}
.card p{font-size:12px;font-weight:300;line-height:15px;margin-bottom:18px}
.sources{display:flex;justify-content:center;gap:14px;align-items:flex-start;font-size:10px;color:var(--dim)}
.source{display:flex;flex-direction:column;align-items:center;gap:3px;white-space:nowrap;min-width:44px}
.source .dot{width:26px;height:26px;border-radius:50%;background:#273047}
.source.on{color:var(--ink)}
.source.on .dot{background:#3a7bf2}
.source.on span{border-bottom:1px solid var(--pink);padding-bottom:2px}
.badges{display:flex;justify-content:center;gap:22px}
.badge{width:36px;height:12px;border-radius:2px;background:#3c4458}
.badge.on{background:#5b4a6c;box-shadow:0 4px 0 -3px var(--pink)}
.card-one{top:1022px}
.card-two{top:1301px}
.trail{left:0;top:0}
.bake-now{left:311px;top:1578px;width:127px;height:37px;font-size:14px}
.faq-pill{left:349px;top:1743px;width:51px;height:18px}
.faq{left:89px;width:570px;height:50px;border-bottom:1px solid var(--line);display:flex;align-items:center;gap:16px;padding-left:18px;font-size:12px;font-weight:300}
.tri{width:0;height:0;border-left:10px solid #fff;border-top:7px solid transparent;border-bottom:7px solid transparent}
.foot-brand{left:0;right:0;top:2042px;justify-content:center;font-size:18px}
.col{top:2120px;font-size:8px;font-weight:300;line-height:18px}
.col h3{font-size:12px;font-weight:400;margin-bottom:2px}
.touch{left:438px;top:2120px;width:233px}
.touch h3{text-align:center;font-size:12px;font-weight:400;margin-bottom:8px}
.field{height:23px;border:1px solid #cfd5e2;border-radius:12px;margin-bottom:9px;font-size:7px;color:var(--dim);padding:0 9px;display:flex;align-items:center;justify-content:space-between}
.submit{margin:4px auto 0;width:51px;height:12px;border-radius:6px;background:linear-gradient(90deg,var(--cyan),var(--lime));color:var(--dark);font-size:7px;display:flex;align-items:center;justify-content:center}
.copy{top:2294px;font-size:8px;font-weight:300}
</style>
</head>
<body>
<div class="page">
  <div class="abs brand site-brand"><span class="brand-mark"></span>loomberrys</div>
  <nav class="abs nav"><a class="active">HOME</a><a>TRY NOVI</a><a>ABOUT US</a></nav>

  <h1 class="abs center headline">Does your company have data that<br>others would find useful?</h1>
  <p class="abs center subhead">Our platform helps you monetize insights<br>without exposing raw data</p>
  <p class="abs center lede">Securely connect your cloud data, and let <b>Novi</b> guide users through Pick Your Own Path<br>insight generation, while keeping your raw data private.</p>
  <div class="abs rule" style="top:387px"></div>

  <p class="abs center intro">Introducing <span class="grad-text">NOVI</span>,<br>our AI Data Concierge.</p>

  <div class="abs glow-frame video">
    <div class="video-fill" role="img" aria-label="Video introducing Novi, the AI data concierge">
      <svg width="14" height="16" viewBox="0 0 14 16"><path d="M0 0L14 8L0 16Z" fill="#fff"/></svg>
    </div>
  </div>
  <div class="abs btn btn-solid demo">Try Web Demo</div>
  <div class="abs btn btn-ghost wait">Join the Waitlist</div>

  <div class="abs pill try-pill">TRY A LOOMBERRY</div>
  <div class="abs glow-frame screen">
    <div class="screen-fill" role="img" aria-label="Screenshot of Novi AI data analyst showing a bar chart and data table"></div>
  </div>
  <svg class="abs arrow" style="left:405px" viewBox="0 0 12 16"><path d="M9 2L3 8L9 14" stroke="#16e6f2" stroke-width="2" fill="none"/></svg>
  <svg class="abs arrow" style="left:708px" viewBox="0 0 12 16"><path d="M3 2L9 8L3 14" stroke="#f4f23c" stroke-width="2" fill="none"/></svg>
  <div class="abs dots"><i class="on"></i><i></i><i></i><i></i><i></i></div>
  <div class="abs sample on" style="left:464px"><div class="shape"></div><span>SMB Accounting</span></div>
  <div class="abs sample off" style="left:568px"><div class="shape round"></div>Campaign Finance</div>

  <div class="abs pill bake-pill">BAKE YOUR OWN LOOMBERRY</div>

  <svg class="abs trail" width="750" height="2324" viewBox="0 0 750 2324">
    <path d="M603 1160C640 1175 668 1210 656 1240C644 1270 580 1275 520 1272C460 1268 410 1268 378 1300" stroke="#f4f23c" stroke-width="2.5" stroke-dasharray="9 8" fill="none"/>
    <path d="M145 1425C110 1440 85 1480 92 1510C102 1548 200 1545 280 1537C330 1532 362 1555 375 1578" stroke="#f4f23c" stroke-width="2.5" stroke-dasharray="9 8" fill="none"/>
  </svg>

  <div class="abs card card-one"><div class="card-in">
    <h2>CONNECT YOUR CLOUD DATA</h2>
    <p>You can connect Novi to your database in a matter of minutes.</p>
    <p>Database Onboarding - A 4-step process where Novi learns your database schema and helps you describe the contents.</p>
    <div class="sources">
      <div class="source"><i class="dot"></i>Zentor</div>
      <div class="source"><i class="dot"></i>Pallomix</div>
      <div class="source"><i class="dot"></i>Brivane KLX</div>
      <div class="source on"><i class="dot"></i><span>Quarion</span></div>
    </div>
  </div></div>

  <div class="abs card card-two"><div class="card-in">
    <h2>CHOOSE DATA SECURITY SETTINGS</h2>
    <p>Novi is designed so that your company's private data is never seen by or fed into an LLM.</p>
    <p>Easily join your data with commonly useful 3rd-party sources, like the Civic Tally or Places of Interest</p>
    <div class="badges"><i class="badge"></i><i class="badge on"></i></div>
  </div></div>

  <div class="abs btn btn-solid bake-now">BAKE NOW</div>

  <div class="abs pill faq-pill">FAQ</div>
  <div class="abs faq" style="top:1773px"><i class="tri"></i>How does NOVI work if I don't give her my data ?</div>
  <div class="abs faq" style="top:1823px"><i class="tri"></i>How is NOVI different from QuillMate ?</div>
  <div class="abs faq" style="top:1873px"><i class="tri"></i>How accurate is NOVI ?</div>

  <div class="abs rule" style="top:2026px"></div>
  <div class="abs brand foot-brand"><span class="brand-mark"></span>loomberrys</div>

  <div class="abs col" style="left:78px"><h3>NOVI</h3>Web Demo</div>
  <div class="abs col" style="left:172px"><h3>COMPANY</h3>About Us<br>Contact</div>
  <div class="abs col" style="left:289px"><h3>OTHER</h3>Terms of Services<br>Privacy Policy<br>Zentor API Disclosure</div>
  <div class="abs touch">
    <h3>GET IN TOUCH</h3>
    <div class="field">Name</div>
    <div class="field">Email Address</div>
    <div class="field">How would you describe your organization?<span style="color:#cfd5e2">&#9662;</span></div>
    <div class="submit">SUBMIT</div>
  </div>
  <p class="abs center copy">&copy; Loomberrys</p>
</div>
</body>
</html>
```